Poly Bag Packaging Motorcycle Cables - Veronzo Brand

Poly Bag Dimensions: 33cm(H) x 24cm(W)
We would like to design a genuine Poly Bag Packaging for motorcycle cables.
Veronzo, is one of the leading companies for manufacturing Motorcycles, located in Egypt. Our company is offering high-quality products, the best in the local market, with very competitive prices.
We have a limited time to get this project done, So we Highly appreciate receiving your designs ASAP.
Target Market(s)
Motorcycle Spare parts Buyers
Font styles to use
Colors
Designer to choose colors to be used in the design.
Look and feel
Each slider illustrates characteristics of the customer's brand and the style your logo design should communicate.

```html
<!DOCTYPE html>
<html lang="en">
<head>
<meta charset="utf-8">
<title>Veronzo Throttle Cable Poly Bag</title>
<link rel="stylesheet" href="https://fonts.googleapis.com/css2?family=Saira+Condensed:wght@500;700&display=swap">
<style>
  :root {
    --page-bg: #efeff0;
    --bag-face: #e3e3e5;
    --header-black: #1c1c1e;
    --header-grey: #3a3a3d;
    --silver-light: #f2f2f4;
    --silver-mid: #a9abb0;
    --silver-dark: #5c5e63;
    --navy: #1d1f5e;
    --navy-deep: #11123c;
    --text-light: #f4f4f8;
    --text-soft: #d8d9ea;
  }
  html, body {
    margin: 0;
    padding: 0;
    width: 1200px;
    height: 1008px;
    overflow: hidden;
    background: var(--page-bg);
  }
  .bag-face {
    position: absolute;
    left: 255px;
    top: 60px;
    width: 690px;
    height: 888px;
    box-shadow: 0 6px 18px rgba(0, 0, 0, 0.18);
  }
  .bag-face svg { display: block; }
  .brand-name {
    font-family: "Saira Condensed", sans-serif;
    font-weight: 700;
    font-size: 62px;
    letter-spacing: 4px;
    fill: var(--silver-mid);
  }
  .product-title {
    font-family: "Saira Condensed", sans-serif;
    font-weight: 500;
    font-size: 30px;
    letter-spacing: 0.8px;
    fill: var(--text-light);
  }
  .product-fit {
    font-family: "Saira Condensed", sans-serif;
    font-weight: 500;
    font-size: 21px;
    letter-spacing: 0.4px;
    fill: var(--text-soft);
  }
</style>
</head>
<body>
  <div class="bag-face">
    <svg width="690" height="888" viewBox="0 0 690 888" xmlns="http://www.w3.org/2000/svg">
      <defs>
        <linearGradient id="header-fill" x1="0" y1="0" x2="1" y2="1">
          <stop offset="0" stop-color="var(--header-black)"/>
          <stop offset="0.6" stop-color="var(--header-grey)"/>
          <stop offset="1" stop-color="var(--header-black)"/>
        </linearGradient>
        <linearGradient id="silver-band" x1="0" y1="0" x2="1" y2="0">
          <stop offset="0" stop-color="var(--silver-dark)"/>
          <stop offset="0.5" stop-color="var(--silver-light)"/>
          <stop offset="0.8" stop-color="var(--silver-mid)"/>
          <stop offset="1" stop-color="var(--silver-dark)"/>
        </linearGradient>
        <linearGradient id="footer-fill" x1="0" y1="0" x2="1" y2="1">
          <stop offset="0" stop-color="var(--navy-deep)"/>
          <stop offset="0.4" stop-color="var(--navy)"/>
          <stop offset="1" stop-color="var(--navy-deep)"/>
        </linearGradient>
        <radialGradient id="product-area" cx="0.5" cy="0.5" r="0.6">
          <stop offset="0" stop-color="#f2f2f3"/>
          <stop offset="1" stop-color="#d9d9dc"/>
        </radialGradient>
        <linearGradient id="badge-fill" x1="0" y1="0" x2="0" y2="1">
          <stop offset="0" stop-color="#c9cace"/>
          <stop offset="0.5" stop-color="#6e7075"/>
          <stop offset="1" stop-color="#3b3c40"/>
        </linearGradient>
      </defs>

      <rect class="face-bg" width="690" height="888" fill="var(--bag-face)"/>

      <rect class="product-window" x="40" y="110" width="610" height="640" fill="url(#product-area)"
            role="img" aria-label="Coiled black motorcycle throttle cable"/>

      <g class="header-band">
        <path d="M0 0 H690 V318 C520 150 250 95 0 103 Z" fill="url(#header-fill)"/>
        <path d="M0 103 C250 95 520 150 690 318 L690 346 C515 170 250 110 0 110 Z" fill="url(#silver-band)"/>
        <text class="brand-name" x="308" y="78" text-anchor="middle">VERONZO</text>
        <circle cx="520" cy="56" r="40" fill="var(--silver-mid)"/>
      </g>

      <g class="footer-band">
        <path d="M0 590 C120 700 420 765 690 782 V888 H0 Z" fill="url(#footer-fill)"/>
        <path d="M0 560 C120 680 420 752 690 768 L690 782 C420 765 120 700 0 590 Z" fill="url(#silver-band)"/>
        <text class="product-title" x="39" y="815">MOTORCYCLE THROTTLE CABLE</text>
        <text class="product-fit" x="39" y="845">Scooter Moped&#160; VZ VR110 T150</text>
        <rect class="quality-badge" x="577" y="708" width="84" height="142" rx="6" fill="url(#badge-fill)" stroke="#2a2b2e" stroke-width="2"/>
      </g>
    </svg>
  </div>
</body>
</html>
```